I would like to update my one-page service sheet to provide a more professional/polished look and...

One page service sheet - with content on both the front and back. I've uploaded my current one page service sheet to provide background. I've also included a service sheet that I recently received from another business owner (from a very different business) that is a representation of the kind of feel I'm looking for. My business website may be found at: www.torvilunconsulting.com

```html
<!DOCTYPE html>
<html lang="en">
<head>
<meta charset="utf-8">
<title>Torvilun Consulting – Service Sheet</title>
<link href="https://fonts.googleapis.com/css2?family=Montserrat:wght@500;600;700&family=Raleway:ital,wght@0,300;0,400;0,500;0,600;0,700;1,500&display=swap" rel="stylesheet">
<style>
:root{
  --stage:#959595;
  --paper:#ffffff;
  --orange:#f26a10;
  --navy:#34465a;
  --ink:#2b3a4a;
  --body:#3c3c3c;
  --white:#ffffff;
}
*{margin:0;padding:0;box-sizing:border-box}
html,body{width:1200px;height:970px;overflow:hidden}
body{background:var(--stage);font-family:'Raleway',sans-serif;position:relative}
.sheet{position:absolute;top:146px;width:522px;height:676px;background:var(--paper);box-shadow:0 4px 10px rgba(0,0,0,.35);overflow:hidden}
.sheet--front{left:56px}
.sheet--back{left:625px}

/* front */
.hero{position:absolute;left:0;top:0;width:522px;height:282px;
  background:linear-gradient(180deg,#233246 0%,#4b4a58 30%,#c77a43 55%,#e79a52 64%,#5a4a48 78%,#1e1e22 100%)}
.brand{position:absolute;left:34px;top:30px;display:flex;align-items:center;gap:8px}
.brand__mark{width:14px;height:14px;background:var(--orange)}
.brand__name{font-family:'Montserrat',sans-serif;font-weight:700;font-size:19px;letter-spacing:.5px;color:var(--white)}
.headline{position:absolute;left:34px;top:170px;color:var(--white);font-weight:300;font-size:22.5px;line-height:28px;letter-spacing:.2px}
.headline strong{font-weight:700}
.service{position:absolute;top:290px;width:150px}
.service--strategy{left:29px}.service--process{left:185px}.service--solutions{left:342px}
.service__photo{height:86px}
.service__photo--hikers{background:linear-gradient(180deg,#3b5876 0%,#d98a48 45%,#f1b15c 60%,#2b2a30 100%)}
.service__photo--jets{background:linear-gradient(160deg,#2c72b4 0%,#6aa7d8 55%,#b9d6ec 100%)}
.service__photo--tech{background:radial-gradient(circle at 50% 60%,#5fa4e0 0%,#1d3f72 45%,#0b1630 100%)}
.service__body{margin-top:4px;height:263px;background:var(--orange);color:var(--white);padding:9px 8px 0 11px}
.service__title{font-family:'Montserrat',sans-serif;font-weight:600;font-size:10.2px;line-height:12px;text-transform:uppercase}
.service__lede{font-style:italic;font-weight:500;font-size:8.1px;line-height:10px;margin-top:1px}
.service__list{margin-top:12px;list-style:none}
.service__list li{position:relative;padding-left:7px;font-size:7.7px;line-height:9.6px;font-weight:400;margin-bottom:3px}
.service__list li::before{content:"•";position:absolute;left:0}
.front-url{position:absolute;left:0;width:522px;top:652px;text-align:center;font-family:'Montserrat',sans-serif;font-weight:600;font-size:10.5px;color:var(--ink)}

/* back */
.story{position:absolute;left:39px;top:22px;width:288px;color:var(--body);font-size:8.3px;line-height:10.2px;text-align:justify}
.story h1{font-weight:400;font-size:25px;line-height:28px;color:var(--ink);margin-bottom:8px;text-align:left}
.story h2{font-family:'Montserrat',sans-serif;font-weight:600;font-size:10px;color:var(--ink);margin:6px 0 12px}
.story p{margin-bottom:10px}
.story a{color:var(--ink);font-weight:700;text-decoration:none}
.approach{position:absolute;left:341px;top:27px;width:150px;height:536px;background:var(--orange);color:var(--white);padding:12px 8px 0 12px;font-size:7.3px;line-height:9.2px}
.approach h2{font-weight:400;font-size:24px;line-height:27px;margin-bottom:7px}
.approach p{margin-bottom:7px}
.approach ul{list-style:none;margin-bottom:7px}
.approach li{position:relative;padding-left:7px;color:var(--ink);font-weight:600;margin-bottom:2px}
.approach li::before{content:"•";position:absolute;left:0}
.contact{position:absolute;left:39px;top:570px;width:452px;height:106px;background:var(--navy);color:var(--white);font-family:'Montserrat',sans-serif;font-weight:600;font-size:10.4px;line-height:12.4px}
.office{position:absolute;top:14px}
.office--mpls{right:252px;text-align:right}
.office--stp{left:250px}
.contact__lines{position:absolute;top:60px;left:0;width:452px;text-align:center}
</style>
</head>
<body>

<section class="sheet sheet--front">
  <div class="hero" role="img" aria-label="Photo of a runner leaping across a rocky summit at sunset above mountains"></div>
  <div class="brand"><span class="brand__mark"></span><span class="brand__name">TORVILUN CONSULTING</span></div>
  <h1 class="headline">REPLACE CONFUSION<br>AND HESITATION<br>WITH <strong>CLARITY AND RESOLVE.</strong></h1>

  <article class="service service--strategy">
    <div class="service__photo service__photo--hikers" role="img" aria-label="Photo of hikers silhouetted on a ridge at sunrise"></div>
    <div class="service__body">
      <h2 class="service__title">Growth Strategy &amp;<br>Innovation</h2>
      <p class="service__lede">Discover what's needed to reach the next stage of growth.</p>
      <ul class="service__list">
        <li>Growth Strategy &amp; Business Model Review. Gain an objective perspective on your growth strategy and business.</li>
        <li>Revenue Acceleration &amp; Lead Generation. Define and execute strategies and tactics to drive demand and top line growth.</li>
        <li>Execution and Scale. Enable your people, processes, and technology to meet the demands of growth.</li>
        <li>Pricing Strategies. Strategically price products and services.</li>
        <li>Growth Training. Group and individual training/coaching.</li>
      </ul>
    </div>
  </article>

  <article class="service service--process">
    <div class="service__photo service__photo--jets" role="img" aria-label="Photo of jets in formation trailing smoke against a blue sky"></div>
    <div class="service__body">
      <h2 class="service__title">Growth Process &amp;<br>Execution</h2>
      <p class="service__lede">Fine-tune and formalize growth processes for efficiency, effectiveness, and scale.</p>
      <ul class="service__list">
        <li>Innovation Capture &amp; Elaboration. Standardize idea capture, analysis, funding, elaboration, and innovation roll-out.</li>
        <li>Growth Channel Optimization. Enhance the prospect and customer experience by blending digital and traditional.</li>
        <li>Business Development. Transform business development into a proactive "team sport" and increase accountability.</li>
        <li>Prospect &amp; Client Experience Mapping. Create greater client stickiness, brand resonance, &amp; be "easier to do business with."</li>
      </ul>
    </div>
  </article>

  <article class="service service--solutions">
    <div class="service__photo service__photo--tech" role="img" aria-label="Photo of hands holding a tablet with glowing digital icons"></div>
    <div class="service__body">
      <h2 class="service__title">Growth Solutions &amp;<br>Analytics</h2>
      <p class="service__lede">Get the right capabilities in place to support your growth journey.</p>
      <ul class="service__list">
        <li>Technology Strategy &amp; Roadmap. Ensure that the right technology is in place for each step of your growth journey.</li>
        <li>Software Selection. Identify the specific capabilities and vendors that are most appropriate for your business.</li>
        <li>Project Leadership. Get critical projects over the finish line.</li>
        <li>Disruptive Trends. Demystify "Digital," "Big Data," "Artificial Intelligence," and "Internet of Things" to create advantage.</li>
        <li>Critical Metrics. Determine the leading and lagging metrics that are most critical for your business.</li>
      </ul>
    </div>
  </article>

  <p class="front-url">www.torvilunconsulting.com</p>
</section>

<section class="sheet sheet--back">
  <div class="story">
    <h1>OUR STORY</h1>
    <p>Torvilun Consulting is a Twin Cities based growth innovation, execution, and solutions consultancy. Our singular focus is on helping businesses reach the next stage of growth - safely and successfully.</p>
    <p>Our name is based on the combination of two words:</p>
    <p>Torv = To move, climb, or go upward</p>
    <p>Ilun = derived from the word, "Execution."</p>
    <p>Together, we get Growth Execution - which is what this business is all about.</p>
    <p>When it comes to growth and scale, many organizations take the wrong action, not enough action, or no action at all. We believe that most businesses have answers to their challenges somewhere inside their walls. But, sometimes, an objective and experienced perspective is helpful to filter and bring to light the most appropriate strategies - and to create accountability so that what needs to get done, actually does.</p>
    <p>While we recognize that growth is serious business, we try to not take ourselves too seriously. A little levity has a way of disarming emotions and facilitating crisper thinking. Our difference is not primarily in the "what" we do, but rather, in the "how" we do it – namely with an intense bias for speed, nimbleness, and objectivity – so that you can achieve your growth objectives.</p>
    <h2>A DIFFERENT CONSULTANCY FOR A NEW ERA</h2>
    <p>A frequent question we get is, "How many employees does Torvilun have?" The answer: 1 to over 100 - depending on how you're counting. We believe that with the exception of a handful of mega consultancies, the traditional "need to own your own" full-time staffing model is a dying a breed. In the new "gig economy" resources and skills are marshaled together in unique configurations to address specific, and often complicated, challenges.</p>
    <p>At Torvilun, we're committed to being a leader in this revolution. We have a team of over 30 highly experienced experts in strategy, technology, process, and program/project management and configure the right team for each unique client situation. In addition, we have strategic partnerships in place with over a half-dozen boutique firms for situations where even heavier lifting is required. Please see a snapshot of the professionals in our ecosystem at: <a>https://torvilunconsulting.com/professionals/</a></p>
    <p>The value to our clients is access to topnotch expertise, specifically selected for their unique need, at a price point that is a fraction of what top tier consultancies charge. We think that makes common sense - and trust that you will, too!</p>
  </div>

  <aside class="approach">
    <h2>OUR<br>APPROACH</h2>
    <p>Most consultancies approach strategy, process, and technology related objectives in silos, but increasingly, businesses need strategies that cut across competencies and business functions.</p>
    <p>At Torvilun, we take a functionally integrated view of our clients' objectives and develop an approach that is agile and actionable. We leverage proven frameworks and techniques and handpick project teams for each client's unique need. The result: practical solutions that balance directional vision with current state realities - and create a path and plan to get from here to there.</p>
    <p>Some key philosophies include:</p>
    <ul>
      <li>Top-down + bottom-up approach.</li>
      <li>Internal + external view of circumstances that is both experiential and balanced with research.</li>
      <li>Bias for getting to the heart of the issue or debate vs. skimming the surface.</li>
      <li>Incremental, hypothesis based approach vs. "betting the farm."</li>
      <li>"Top 3 Priorities" focus to maximize speed to impact and value - and to get smarter as we move forward.</li>
      <li>Addressing the problem as it is vs. the problem how we wish it were.</li>
      <li>Intense focus on speed to value.</li>
    </ul>
    <p>If this approach could benefit your business and you're looking for another perspective, we'd welcome the opportunity to discuss.</p>
  </aside>

  <footer class="contact">
    <div class="office office--mpls">MINNEAPOLIS<br>5120 West 82nd St, Ste 14,<br>Edina, MN 55437</div>
    <div class="office office--stp">ST. PAUL<br>381 Harwell Dr, Ste 9,<br>Woodbury, MN 55129</div>
    <div class="contact__lines">(651) 555-0148<br>admin@torvilunconsulting.com<br>www.torvilunconsulting.com</div>
  </footer>
</section>

</body>
</html>
```